Zappo! Dog Training & Boarding School

I need a brochure that makes people aware of the dog training services I offer. This includes:
Group Classes
Private lessons
Help with Behavior Problems
Boarding School
.See my website: www.zappodogtraining.com

Target Market(s)

People with dogs

Industry/Entity Type

School

Font styles to use
Serif

Requirements
Must have
• My Logo and Tag line. Must be trifold brochure. Include brief description of services and training philosophy, a little info about me and some important lines from testimonials. I like bright colors, pics of happy dogs and happy people.
Nice to have
• I thought it would be cool to have something on the cover where there are people seeming saying "What do want? Well mannered dogs! How do we get them? Zappo! Dog Training" Then a group of dogs saying "What do we want? People we understand! How do we get them? Zappo! Dog Training"

```html
<!DOCTYPE html>
<html lang="en">
<head>
<meta charset="utf-8">
<title>Zappo! Dog Training – Trifold Brochure</title>
<link rel="stylesheet" href="https://fonts.googleapis.com/css2?family=Open+Sans:wght@400;600;700&family=Tenor+Sans&display=swap">
<style>
  :root {
    --green-light: #8cc63f;
    --green: #5aa832;
    --green-dark: #3f8a23;
    --blue-light: #3fb3e6;
    --blue: #1f8fd3;
    --blue-dark: #1565b0;
    --white: #ffffff;
    --yellow: #f2c418;
    --orange: #f08a1c;
    --page-bg: #e4e4e4;
  }
  * { box-sizing: border-box; margin: 0; padding: 0; }
  html, body { width: 1200px; height: 855px; overflow: hidden; background: var(--page-bg); }
  body { font-family: "Open Sans", Arial, sans-serif; color: var(--white); }

  .brochure { position: absolute; left: 0; top: 0; width: 1200px; height: 855px; display: flex; }
  .panel { position: relative; width: 400px; height: 855px; overflow: hidden; }

  /* About panel */
  .panel--about { background: linear-gradient(180deg, var(--green-light) 0%, var(--green) 60%, var(--green-dark) 100%); }
  .about__photo { position: absolute; left: 0; top: 0; width: 400px; height: 300px; }
  .about__body { position: absolute; left: 30px; top: 315px; width: 345px; font-size: 13px; line-height: 1.3; }
  .about__title { font-weight: 700; font-size: 14.5px; letter-spacing: .5px; margin-bottom: 10px; }
  .about__body p { margin-bottom: 12px; }
  .about__dog { position: absolute; left: 0; bottom: 0; width: 185px; height: 185px; border-radius: 0 60px 0 0; background: radial-gradient(circle at 50% 55%, #c9905a 0%, #8a5a33 55%, #6f9c3a 100%); }
  .about__badges { position: absolute; left: 270px; top: 676px; display: flex; gap: 10px; }
  .badge { width: 44px; height: 44px; border-radius: 50%; border: 3px solid var(--white); }
  .badge--blue { background: var(--blue-dark); }
  .badge--gold { background: var(--yellow); }
  .about__contact { position: absolute; left: 200px; top: 735px; width: 190px; font-size: 12.5px; line-height: 1.35; font-style: normal; }
  .about__hello { font-family: "Tenor Sans", sans-serif; font-size: 20px; white-space: nowrap; margin-bottom: 5px; }

  /* Testimonials panel */
  .panel--testimonials { background: linear-gradient(180deg, var(--blue-dark) 0%, var(--blue) 40%, var(--blue-light) 100%); }
  .testimonials__title { position: absolute; left: 30px; top: 40px; font-weight: 700; font-size: 14px; line-height: 1.3; letter-spacing: .3px; }
  .photo-frame { position: absolute; border: 5px solid var(--white); box-shadow: 0 3px 8px rgba(0,0,0,.35); }
  .testimonials__group { left: 190px; top: 30px; width: 180px; height: 120px; background: linear-gradient(160deg, #7aa060, #4d6e3c 60%, #8c7a60); transform: rotate(2deg); }
  .quote { position: absolute; left: 30px; width: 345px; font-size: 11.5px; line-height: 1.3; }
  .quote--one { top: 180px; }
  .quote--two { top: 400px; }
  .quote--three { top: 692px; }
  .quote__by { display: block; margin-top: 2px; }
  .testimonials__pup { left: 40px; top: 560px; width: 155px; height: 105px; background: radial-gradient(circle at 50% 55%, #f2e4d2, #c09070 55%, #5f8a3a); transform: rotate(-6deg); }
  .testimonials__pack { left: 180px; top: 545px; width: 185px; height: 125px; background: linear-gradient(170deg, #d9cfc0 0%, #a87d5c 45%, #6aa03a 100%); transform: rotate(5deg); }

  /* Cover panel */
  .panel--cover { background: var(--white); }
  .cover__header { position: absolute; left: 0; top: 0; width: 400px; height: 130px; background: linear-gradient(90deg, var(--blue) 0%, var(--blue-light) 100%); }
  .cover__brand { position: absolute; left: 30px; top: 32px; display: flex; align-items: center; gap: 12px; }
  .cover__brand-mark { width: 36px; height: 36px; border-radius: 50%; background: var(--yellow); }
  .cover__brand-name { font-family: "Open Sans", Arial, sans-serif; font-weight: 600; font-size: 26px; color: var(--white); }
  .cover__tagline { position: absolute; left: 78px; top: 80px; font-size: 13px; }
  .cover__photo { position: absolute; left: 0; top: 130px; width: 400px; height: 440px; background: linear-gradient(180deg, #c9c0ac 0%, #9e7b52 45%, #b98956 60%, #3f7a3a 100%); }
  .bubble { position: absolute; border-radius: 40px; display: flex; align-items: center; justify-content: center; text-align: center; font-weight: 700; line-height: 1.1; border: 3px solid var(--white); }
  .bubble--want { left: 20px; top: 150px; width: 100px; height: 58px; font-size: 11px; background: var(--green-light); }
  .bubble--people { left: 130px; top: 145px; width: 150px; height: 76px; font-size: 16px; background: var(--blue); }
  .bubble--how { left: 282px; top: 140px; width: 100px; height: 58px; font-size: 11px; background: var(--orange); }
  .cover__footer { position: absolute; left: 0; top: 540px; width: 400px; height: 315px; }
  .cover__name { position: absolute; left: 0; top: 610px; width: 400px; text-align: center; font-family: "Tenor Sans", sans-serif; font-weight: 400; font-size: 32px; }
  .cover__role { position: absolute; left: 0; top: 655px; width: 400px; text-align: center; font-family: "Tenor Sans", sans-serif; font-size: 18px; opacity: .9; }
  .cover__phone { position: absolute; left: 0; top: 690px; width: 400px; display: flex; justify-content: center; align-items: center; gap: 10px; font-size: 26px; font-weight: 600; }
  .cover__web { position: absolute; left: 0; top: 765px; width: 400px; height: 44px; background: var(--blue); display: flex; align-items: center; justify-content: center; font-size: 18px; font-weight: 600; letter-spacing: .5px; }
</style>
</head>
<body>
<main class="brochure">

  <section class="panel panel--about">
    <svg class="about__photo" viewBox="0 0 400 300" role="img" aria-label="Photo of the trainer smiling in a grassy field with three small dogs">
      <defs>
        <linearGradient id="fieldTone" x1="0" y1="0" x2="0" y2="1">
          <stop offset="0" stop-color="#8fbf6a"/>
          <stop offset=".5" stop-color="#5e9a3c"/>
          <stop offset="1" stop-color="#4a8a30"/>
        </linearGradient>
      </defs>
      <path d="M0 0H400V230Q200 300 0 285Z" fill="url(#fieldTone)"/>
      <path d="M0 285Q200 300 400 230" fill="none" stroke="#ffffff" stroke-width="5"/>
    </svg>
    <div class="about__body">
      <h2 class="about__title">ABOUT MARLA KENNING</h2>
      <p>For as long as I can remember I’ve had a passion for animals and felt comforted by their presence.</p>
      <p>Having moved many times as a child, I often took comfort in being outdoors, creating relationships with a menagerie of scaled, shelled, feathered and furry critters that were never far from my home. At night, my favorite stuffed animals would keep the monster under my bed at bay. Dogs have been some of my very best friends over the years… and every pet has been like a family member.</p>
      <p>I also discovered that a ‘free spirit’ dog with some training actually ends up being more free. Here’s what happens: When dogs are well-behaved, they’re welcomed in more places, and when they can be trusted to follow a few simple cues, we tend to give them more freedom than we did before.</p>
    </div>
    <div class="about__dog" role="img" aria-label="Close-up photo of a happy brown and white dog"></div>
    <div class="about__badges">
      <span class="badge badge--blue"></span>
      <span class="badge badge--gold"></span>
    </div>
    <address class="about__contact">
      <div class="about__hello">Woof! Say Hello!</div>
      312 Alder Creek Rd<br>
      Pine Hollow, CA 95000<br>
      831-555-0142
    </address>
  </section>

  <section class="panel panel--testimonials">
    <h2 class="testimonials__title">ZAPPO!<br>DOG TRAINING<br>TESTIMONIALS</h2>
    <div class="photo-frame testimonials__group" role="img" aria-label="Group photo of happy class graduates with their dogs"></div>
    <p class="quote quote--one">Some dog trainers are terrific with people. Some dog trainers have an amazing understanding of dogs, and what motivates them. Sadly, not many dog trainers possess both of these qualities. Marla does. How do I know? Because I have taken 3 classes from her with my dog Mazie, and she is the best. This is my third dog, and I have used other trainers in the past, but none had the excellent communication skills that Marla has. She communicates clearly, breaks things down into manageable tasks, gives invaluable feedback, and makes training fun! Her handouts and web site contain enormous amounts of useful information, and I find myself referring back to them months after a class has ended.<br>Thanks, Zappo Dog Training! We’ll be back for more!<span class="quote__by">*** Denise ***</span></p>
    <p class="quote quote--two">We have taken 3 classes with Zappo Dog Training with 2 different dogs. Zappo teaches how to communicate with dogs using positive reinforcement—the dog learns to listen to you because it is rewarding. The homework assignments are great, and the results are impressive. It really gets addictive to teach stuff to your dog once you learn to get its attention through rewards.<span class="quote__by">*** Ramon ***</span></p>
    <div class="photo-frame testimonials__pup" role="img" aria-label="Photo of a playful puppy on the grass"></div>
    <div class="photo-frame testimonials__pack" role="img" aria-label="Photo of several dogs playing together in a yard"></div>
    <p class="quote quote--three">Zappo Dog Training was really fantastic for our 12 week old puppy, Stanley, and his parents. I believe Marla’s training techniques make total sense. She handles the dogs with a lot of love and enjoyment. She is stern enough to get the point across, but patient enough to give the dogs time to figure out what she is asking them to do. We purchased the puppy package and are looking forward to our next class. Our Stanley is now 6 months old and a joy to have around. Thanks Marla for a great class. *** Tessa ***</p>
  </section>

  <section class="panel panel--cover">
    <div class="cover__photo" role="img" aria-label="Photo of a group of happy dogs sitting together on a porch"></div>
    <header class="cover__header">
      <div class="cover__brand">
        <span class="cover__brand-mark"></span>
        <span class="cover__brand-name">Zappo! Dog Training</span>
      </div>
      <div class="cover__tagline">…happy dogs, happy homes</div>
    </header>
    <div class="bubble bubble--want">What do<br>we want?</div>
    <div class="bubble bubble--people">people who<br>understand us!</div>
    <div class="bubble bubble--how">How do we<br>get them?</div>
    <svg class="cover__footer" viewBox="0 0 400 315" aria-hidden="true">
      <defs>
        <linearGradient id="coverGreen" x1="0" y1="0" x2="0" y2="1">
          <stop offset="0" stop-color="#8cc63f"/>
          <stop offset="1" stop-color="#5aa832"/>
        </linearGradient>
      </defs>
      <path d="M0 60Q200 -10 400 0V315H0Z" fill="url(#coverGreen)"/>
      <path d="M0 60Q200 -10 400 0" fill="none" stroke="#ffffff" stroke-width="6"/>
    </svg>
    <h1 class="cover__name">Marla Kenning</h1>
    <div class="cover__role">Head Woofie Woof</div>
    <div class="cover__phone">
      <svg width="24" height="24" viewBox="0 0 24 24" aria-hidden="true">
        <circle cx="12" cy="12" r="10.5" fill="none" stroke="#ffffff" stroke-width="2"/>
        <path d="M8.5 7.5c.5-.5 1.2-.4 1.5.1l1 1.6c.3.5.2 1-.2 1.4l-.6.5c.5 1.1 1.4 2 2.5 2.5l.5-.6c.4-.4.9-.5 1.4-.2l1.6 1c.5.3.6 1 .1 1.5l-.8.8c-2.8.4-7.6-4.4-7.2-7.2z" fill="#ffffff"/>
      </svg>
      831 555 0142
    </div>
    <div class="cover__web">www.zappodogtraining.com</div>
  </section>

</main>
</body>
</html>
```